A church planting organization designed specifically for the urban centers

I am looking to create a 5 page website.

i would like to create an (1) Homepage, (2) About Us, (3) Donate, (4) Contact Us, and (5) Partner Page

The name of the organization is called Harbor Lantern Seedworks which is an organization designed to help establish churches in a central city context.

I would like the colors to incorporate the colors of the logo which is a black, white, and orange. I would be okay with adding a
green for an accent. I love the use of orange filters when appropriate.

We would like to have a design that pops at first glance. I have included some graphs that can be recreated or recolored to better fit with one's design.

Primary Goal:
A marketing tool to attract (1) Harbor Lantern Seedworks who desire to plant and; (2) donors; (3) churches or church plant networks that have an interest in partnering financially or through collective impact. Information should be provided on how to become part of the movement.

Secondary Goal:
Make the argument why central city church plants are needed
Make the argument why Multi-Ethnic churches are needed
Candidates can apply for residency at one of the network churches
Churches can apply to join the network
Church Planting Networks can apply to partner

Target Market(s)

Target Market
Church Planting Networks
Ethnic Homogenous Churches
Church Networks
Church Planters
Diversity Seekers
Impactors of Distressed Communities

Coding

Number of Pages Required

Font styles to use
Other font styles liked:
• I have uploaded our font

Requirements
Must have
• Pages that pop at first glance
Nice to have
• I would like the graphs I attached recreated or recolored to match your design layout

```html
<!DOCTYPE html>
<html lang="en">
<head>
<meta charset="UTF-8">
<title>Harbor Lantern Seedworks</title>
<link href="https://fonts.googleapis.com/css2?family=Montserrat:wght@300;400;600;700;800&family=Roboto:wght@400;500;700&display=swap" rel="stylesheet">
<style>
:root{
  --orange:#ec6a1f;
  --orange-deep:#d9591a;
  --ink:#0b0b12;
  --night:#07070f;
  --charcoal:#2b2b2b;
  --smoke:#454545;
  --paper:#f3f3f3;
  --white:#ffffff;
  --footer:#1d1d1d;
}
*{margin:0;padding:0;box-sizing:border-box}
html,body{width:1200px;height:3934px;overflow:hidden}
body{position:relative;font-family:'Roboto',sans-serif;background:var(--white);color:var(--ink)}
.abs{position:absolute}
.heading{font-family:'Montserrat',sans-serif;font-weight:300;letter-spacing:.5px}
.heading b{font-weight:800}

/* header */
.site-header{position:absolute;left:0;top:0;width:1200px;height:93px;background:var(--white);border-top:5px solid var(--orange);z-index:5}
.brand-badge{position:absolute;left:95px;top:-5px;width:150px;height:145px;border-radius:0 0 75px 75px;background:var(--white);display:flex;align-items:center;justify-content:center;flex-direction:column;z-index:6}
.brand-badge .dot{width:14px;height:14px;border-radius:50%;background:var(--orange);margin-bottom:6px}
.brand-badge span{font-family:'Montserrat',sans-serif;font-weight:700;font-size:13px;line-height:1.25;text-align:center;color:var(--ink)}
.nav{position:absolute;top:40px;font-family:'Roboto',sans-serif;font-weight:500;font-size:14px;color:#222}
.nav.active{color:var(--orange)}
.nav.active::after{content:"";position:absolute;left:0;right:0;bottom:-9px;height:2px;background:var(--orange)}
.donate-btn{position:absolute;left:940px;top:29px;width:147px;height:40px;border-radius:20px;background:var(--orange);color:var(--white);font-weight:700;font-size:14px;display:flex;align-items:center;justify-content:center;gap:8px}

/* hero */
.hero{position:absolute;left:0;top:93px;width:1200px;height:556px;background:var(--night)}
.hero-photo{position:absolute;left:560px;top:0;width:640px;height:556px;background:linear-gradient(100deg,var(--night) 0%,#2a3320 22%,#6b7a55 45%,#3a3124 70%,#7a6430 88%,#2a2015 100%)}
.hero-title{position:absolute;left:110px;top:258px;font-family:'Montserrat',sans-serif;font-weight:800;font-size:50px;line-height:54px;color:var(--white)}
.hero-title .accent{color:var(--orange)}
.hero-text{position:absolute;left:111px;top:385px;width:460px;font-size:16px;font-weight:500;line-height:27px;color:var(--white)}
.btn-orange{position:absolute;left:111px;top:470px;width:289px;height:49px;border-radius:25px;background:var(--orange);color:var(--white);font-weight:700;font-size:15px;display:flex;align-items:center;justify-content:center}

/* mission */
.mission{position:absolute;left:0;top:649px;width:1200px;height:360px;background:var(--night)}
.mission-brand{position:absolute;left:155px;top:40px;width:222px;height:206px;display:flex;flex-direction:column;align-items:center;justify-content:center;gap:10px}
.mission-brand .ring{width:60px;height:60px;border-radius:50%;border:5px solid var(--white)}
.mission-brand span{font-family:'Montserrat',sans-serif;font-weight:700;font-size:20px;color:var(--white);text-align:center;line-height:1.25}
.mission h2{position:absolute;left:453px;top:80px;font-size:38px;color:var(--white)}
.mission p{position:absolute;left:453px;top:145px;width:600px;font-size:15px;line-height:26px;color:var(--white)}

/* problem */
.problem{position:absolute;left:0;top:900px;width:1200px;height:612px}
.problem-bg{position:absolute;inset:0;background:linear-gradient(180deg,var(--orange) 0%,#e2631f 60%,#c95a1e 100%)}
.problem h2{position:absolute;left:0;width:1200px;top:100px;text-align:center;font-size:38px;color:var(--white)}
.problem-copy{position:absolute;left:140px;top:160px;width:920px;text-align:center;color:var(--white);font-size:14px;line-height:25px}
.problem-copy p{margin-bottom:12px}
.btn-white{position:absolute;left:505px;top:468px;width:190px;height:46px;border-radius:23px;background:var(--white);color:var(--orange);font-weight:500;font-size:14px;display:flex;align-items:center;justify-content:center;gap:8px}

/* barrier */
.barrier{position:absolute;left:0;top:1512px;width:1200px;height:360px;background:linear-gradient(180deg,#3b3b3b,#2a2a2a 60%,#333)}
.barrier h2{position:absolute;left:0;width:1200px;top:66px;text-align:center;font-size:38px;color:var(--white)}
.barrier-item{position:absolute;top:160px;width:220px;text-align:center;color:var(--white);font-weight:700;font-size:15px;line-height:24px}
.barrier-item svg{display:block;margin:0 auto 18px}

/* partner */
.partner{position:absolute;left:0;top:1872px;width:1200px;height:940px;background:var(--paper)}
.partner h2{position:absolute;left:0;width:1200px;top:62px;text-align:center;font-size:38px;color:var(--ink)}
.partner-label{position:absolute;font-weight:500;font-size:16px;color:var(--ink)}

/* faq */
.faq{position:absolute;left:0;top:2765px;width:1200px;height:808px}
.faq h2{position:absolute;left:0;width:1200px;top:105px;text-align:center;font-size:38px;color:var(--white)}
.faq h2 .accent{color:var(--orange);font-weight:300}
.faq-item{position:absolute;left:185px;width:832px;height:47px;border-radius:14px;background:rgba(160,160,160,.55);display:flex;align-items:center;padding:0 24px 0 32px;font-weight:500;font-size:14px;color:var(--white)}
.faq-item .q{color:var(--orange);margin-right:8px}
.faq-item .chev{margin-left:auto;width:13px;height:13px;border-radius:50%;background:var(--orange);display:flex;align-items:center;justify-content:center}

/* footer */
.site-footer{position:absolute;left:0;top:3573px;width:1200px;height:361px;background:var(--footer);color:var(--white)}
.site-footer h4{position:absolute;top:65px;font-size:18px;font-weight:700}
.contact-line{position:absolute;left:110px;font-size:14px;line-height:22px;display:flex;gap:12px}
.contact-line svg{flex:none;margin-top:4px}
.link{position:absolute;font-size:14px}
.email-field{position:absolute;left:733px;top:113px;width:235px;height:43px;border-radius:22px;background:var(--white);font-size:11px;color:#999;padding:14px 22px}
.submit-btn{position:absolute;left:983px;top:113px;width:122px;height:43px;border-radius:22px;background:var(--orange);font-weight:700;font-size:16px;display:flex;align-items:center;justify-content:center}
.consent{position:absolute;left:729px;top:178px;font-size:13px;font-weight:500;display:flex;gap:8px;align-items:center}
.social{position:absolute;top:217px;width:31px;height:31px;border-radius:50%;border:1px solid var(--white)}
.copyright{position:absolute;left:0;width:1200px;top:316px;text-align:center;font-size:13px}
</style>
</head>
<body>

<header class="site-header">
  <div class="brand-badge"><div class="dot"></div><span>Harbor Lantern<br>Seedworks</span></div>
  <span class="nav active" style="left:503px">HOME</span>
  <span class="nav" style="left:581px">ABOUT US</span>
  <span class="nav" style="left:690px">PARTNERS</span>
  <span class="nav" style="left:801px">CONTACT US</span>
  <div class="donate-btn">
    <svg width="16" height="14" viewBox="0 0 16 14"><path d="M8 14 1.2 7.2A4 4 0 0 1 8 2a4 4 0 0 1 6.8 5.2Z" fill="#fff"/></svg>DONATE
  </div>
</header>

<section class="hero">
  <div class="hero-photo" role="img" aria-label="Preacher standing on a stage in front of a worship screen"></div>
  <h1 class="hero-title" style="top:165px"><span class="accent">HARBOR LANTERN</span><br>SEEDWORKS</h1>
  <p class="hero-text" style="top:292px">The church planting scene in the central city of Milwaukee is fairly problematic.</p>
  <div class="btn-orange" style="top:377px">CHURCH PLANTER INTEREST</div>
</section>

<section class="mission">
  <div class="mission-brand"><div class="ring"></div><span>Harbor Lantern<br>Seedworks</span></div>
  <h2 class="heading"><b>OUR</b> MISSION</h2>
  <p>To multiply the gospel in urban centers by raising up and equipping church planters in a central city or multi-ethnic context.</p>
</section>

<section class="problem">
  <div class="problem-bg" role="img" aria-label="Launch team members with an orange colour filter"></div>
  <svg class="abs" style="left:0;top:0" width="1200" height="100" viewBox="0 0 1200 100">
    <path d="M0 0H1200V94Q600-10 0 94Z" fill="#07070f"/>
    <path d="M0 94Q600-10 1200 94V86Q600-22 0 86Z" fill="#fff"/>
  </svg>
  <h2 class="heading">THE <b>PROBLEM</b></h2>
  <div class="problem-copy">
    <p>Problem-The church planting scene in the central city of Milwaukee is fairly problematic. While church planting networks have been planting many churches in a suburban context each year, the central city has been ignored. Unfortunately, many church planting organizations have little to no understanding of the central city context and have therefore avoided planting central city churches in Milwaukee and beyond.To exacerbate the issue, Black churches historically do not plant churches.</p>
    <p>Subsequently, the central city church planter has been deserted. In many cases, those called to start a church in the central city are left to go at it alone with zero support. It’s not because there’s a lack of churches or church plant organizations available, as there are many. It’s either they don’t see the value in planting central city churches or they don’t have the expertise to do it. Either way, the central city is lacking new gospel centered churches that will reach new generations.</p>
    <p>These generations will be lost if something is not done to create new churches. Consequently, the suburban cookie-cutter approach applied to a central city context commonly ends up in a failed church plant.</p>
  </div>
  <div class="btn-white">LEARN MORE
    <svg width="14" height="14" viewBox="0 0 14 14"><circle cx="7" cy="7" r="7" fill="#ec6a1f"/><path d="M5.5 4 8.5 7 5.5 10" stroke="#fff" stroke-width="2" fill="none"/></svg>
  </div>
</section>

<section class="barrier" role="img" aria-label="Faded city street in grey tones">
  <h2 class="heading"><b>BARRIER</b> TO ADDRESS</h2>
  <div class="barrier-item" style="left:79px">
    <svg width="60" height="62" viewBox="0 0 60 62" fill="#ec6a1f"><rect x="28" y="0" width="4" height="14"/><rect x="23" y="4" width="14" height="4"/><path d="M10 28 30 14 50 28V62H10Z"/><rect x="2" y="34" width="8" height="28"/><rect x="50" y="34" width="8" height="28"/><path d="M24 62V46a6 6 0 0 1 12 0v16Z" fill="#333"/></svg>
    SUBURBAN SUPPORT<br>RAISING MODEL</div>
  <div class="barrier-item" style="left:278px">
    <svg width="66" height="62" viewBox="0 0 66 62" fill="#ec6a1f"><circle cx="33" cy="14" r="11"/><circle cx="12" cy="24" r="8"/><circle cx="54" cy="24" r="8"/><path d="M16 62V42a17 17 0 0 1 34 0v20Z"/><path d="M0 62V46a12 12 0 0 1 14-8v24Z"/><path d="M66 62V46a12 12 0 0 0-14-8v24Z"/></svg>
    LAUNCH TEAM</div>
  <div class="barrier-item" style="left:478px">
    <svg width="58" height="62" viewBox="0 0 58 62" fill="#ec6a1f"><rect x="2" y="6" width="40" height="56" rx="3"/><rect x="14" y="2" width="16" height="8" rx="2"/><path d="M8 22l4 4 7-8M8 38l4 4 7-8" stroke="#333" stroke-width="3" fill="none"/><rect x="24" y="22" width="12" height="3" fill="#333"/><path d="M52 20 58 26 32 52 24 54 26 46Z"/></svg>
    CHURCH PLANTER<br>ASSESSMENT</div>
  <div class="barrier-item" style="left:675px">
    <svg width="62" height="62" viewBox="0 0 62 62" fill="#ec6a1f"><rect x="4" y="4" width="22" height="22" rx="4"/><rect x="36" y="4" width="22" height="22" rx="4"/><rect x="4" y="36" width="22" height="22" rx="4"/><rect x="36" y="36" width="22" height="22" rx="4"/><circle cx="31" cy="31" r="12" fill="#333"/><circle cx="31" cy="31" r="7"/></svg>
    CULTURAL<br>COMPETENCY</div>
  <div class="barrier-item" style="left:876px">
    <svg width="62" height="62" viewBox="0 0 62 62" fill="#ec6a1f"><rect x="4" y="4" width="54" height="42" rx="6"/><path d="M14 46 10 60 28 46Z"/><circle cx="31" cy="25" r="13" fill="#333"/><circle cx="31" cy="25" r="9"/><path d="M31 16V34M31 25 24 31M31 25 38 31" stroke="#333" stroke-width="2.5"/></svg>
    CULTURAL COMMUNICATION<br>PRIORITY</div>
</section>

<section class="partner">
  <div class="abs" style="inset:0;background:linear-gradient(90deg,#e9e9e9,#f7f7f7 50%,#e6e6e6)" role="img" aria-label="Faded portraits of community members in light grey"></div>
  <h2 class="heading"><b>WHY PARTNER</b> WITH HLS</h2>
  <svg class="abs" style="left:0;top:0" width="1200" height="900" viewBox="0 0 1200 900">
    <!-- arc and connectors -->
    <path d="M322 186V309" stroke="#111" stroke-width="4"/>
    <path d="M322 640V762" stroke="#111" stroke-width="4"/>
    <path d="M397 392 450 355" stroke="#111" stroke-width="4"/>
    <path d="M397 592 450 630" stroke="#111" stroke-width="4"/>
    <path d="M429 496H486" stroke="#111" stroke-width="4"/>
    <path d="M264 329A167 167 0 0 1 264 663" stroke="#111" stroke-width="5" fill="none"/>
    <path d="M264 329V333" stroke="#111" stroke-width="5"/>
    <circle cx="264" cy="496" r="148" fill="#111"/>
    <circle cx="264" cy="496" r="120" fill="#fff"/>
    <circle cx="264" cy="496" r="112" fill="none" stroke="#111" stroke-width="3"/>
    <circle cx="264" cy="452" r="12" fill="#ec6a1f"/>
    <text x="264" y="498" text-anchor="middle" font-family="Montserrat, sans-serif" font-weight="700" font-size="19" fill="#111">Harbor Lantern</text>
    <text x="264" y="524" text-anchor="middle" font-family="Montserrat, sans-serif" font-weight="700" font-size="19" fill="#111">Seedworks</text>
    <!-- connector dots -->
    <g fill="#ec6a1f" stroke="#111" stroke-width="3">
      <circle cx="322" cy="339" r="7"/><circle cx="397" cy="392" r="7"/><circle cx="429" cy="496" r="7"/><circle cx="397" cy="602" r="7"/><circle cx="322" cy="651" r="7"/>
    </g>
    <!-- item circles -->
    <g>
      <circle cx="322" cy="226" r="56" fill="#ec6a1f"/><circle cx="322" cy="226" r="44" fill="#fff"/>
      <g fill="none" stroke="#ec6a1f" stroke-width="2.5"><circle cx="308" cy="226" r="6"/><circle cx="336" cy="226" r="6"/><circle cx="322" cy="220" r="6"/><path d="M298 250v-6a10 10 0 0 1 20 0v6zM326 250v-6a10 10 0 0 1 20 0v6zM312 244v-4a10 10 0 0 1 20 0v4"/><path d="M322 198l2 4 4 1-3 3 1 4-4-2-4 2 1-4-3-3 4-1z"/></g>
    </g>
    <g>
      <circle cx="489" cy="328" r="56" fill="#111"/><circle cx="489" cy="328" r="44" fill="#fff"/>
      <g fill="none" stroke="#111" stroke-width="2.5"><path d="M489 298v10M484 302h10M471 318l18-10 18 10v26h-36zM463 326h8v18h-8zM507 326h8v18h-8zM484 344v-10a5 5 0 0 1 10 0v10"/></g>
    </g>
    <g>
      <circle cx="541" cy="496" r="56" fill="#ec6a1f"/><circle cx="541" cy="496" r="44" fill="#fff"/>
      <g fill="none" stroke="#ec6a1f" stroke-width="2.2"><rect x="514" y="476" width="10" height="10"/><circle cx="541" cy="481" r="5"/><rect x="553" y="476" width="10" height="10"/><rect x="514" y="492" width="49" height="10"/><circle cx="541" cy="514" r="5"/><path d="M541 502v7"/></g>
    </g>
    <g>
      <circle cx="489" cy="661" r="56" fill="#111"/><circle cx="489" cy="661" r="44" fill="#fff"/>
      <g fill="none" stroke="#111" stroke-width="2.5"><circle cx="482" cy="658" r="9"/><path d="M466 686v-4a16 16 0 0 1 32 0v4z"/><circle cx="504" cy="640" r="8"/><path d="M500 650h8"/></g>
    </g>
    <g>
      <circle cx="322" cy="762" r="56" fill="#ec6a1f"/><circle cx="322" cy="762" r="44" fill="#fff"/>
      <g fill="none" stroke="#ec6a1f" stroke-width="2.5"><rect x="300" y="740" width="18" height="18" rx="3"/><rect x="326" y="740" width="18" height="18" rx="3"/><rect x="300" y="766" width="18" height="18" rx="3"/><rect x="326" y="766" width="18" height="18" rx="3"/><circle cx="322" cy="762" r="7"/></g>
    </g>
  </svg>
  <span class="partner-label" style="left:417px;top:202px">WE HAVE URBAN CHURCH PLANT EXPERTS</span>
  <span class="partner-label" style="left:588px;top:320px">WE HAVE PLANTED SUCCESFUL URBAN CHURCHES</span>
  <span class="partner-label" style="left:638px;top:488px">WE HAVE AN URBAN CHURCH PLANTER PIPELINE</span>
  <span class="partner-label" style="left:586px;top:664px">WE HAVE INDIGENOUS URBAN LEADERSHIP</span>
  <span class="partner-label" style="left:417px;top:778px">WE HAVE A HIGH LEVEL OF CULUTURAL COMPETENCE</span>
</section>

<section class="faq">
  <div class="abs" style="inset:0;background:linear-gradient(90deg,#4a4a4a,#3f3f3f 55%,#2e2e2e)" role="img" aria-label="Grey-toned row of city houses"></div>
  <svg class="abs" style="left:0;top:0" width="1200" height="808" viewBox="0 0 1200 808">
    <path d="M0 0H1200V92Q600-20 0 92Z" fill="#f3f3f3"/>
    <path d="M0 92Q600-20 1200 92V82Q600-36 0 82Z" fill="#ec6a1f"/>
    <path d="M0 715Q600 820 1200 715V808H0Z" fill="#1d1d1d"/>
    <path d="M0 715Q600 820 1200 715V700Q600 835 0 718Z" fill="#ec6a1f"/>
  </svg>
  <h2 class="heading"><b>HARBOR LANTERN</b> <span class="accent">FAQS</span></h2>
  <div class="faq-item" style="top:200px"><span class="q">Q:</span>Why partner with HLS?<span class="chev"><svg width="7" height="5" viewBox="0 0 7 5"><path d="M1 1l2.5 2.5L6 1" stroke="#fff" fill="none" stroke-width="1.4"/></svg></span></div>
  <div class="faq-item" style="top:268px"><span class="q">Q:</span>Who Do We Partner With?<span class="chev"><svg width="7" height="5" viewBox="0 0 7 5"><path d="M1 1l2.5 2.5L6 1" stroke="#fff" fill="none" stroke-width="1.4"/></svg></span></div>
  <div class="faq-item" style="top:337px"><span class="q">Q:</span>How do my network partner with HLS?<span class="chev"><svg width="7" height="5" viewBox="0 0 7 5"><path d="M1 1l2.5 2.5L6 1" stroke="#fff" fill="none" stroke-width="1.4"/></svg></span></div>
  <div class="faq-item" style="top:405px"><span class="q">Q:</span>Why does HLS work with so many different planting arms?<span class="chev"><svg width="7" height="5" viewBox="0 0 7 5"><path d="M1 1l2.5 2.5L6 1" stroke="#fff" fill="none" stroke-width="1.4"/></svg></span></div>
  <div class="faq-item" style="top:473px"><span class="q">Q:</span>Do HLS only work with minority church planters?<span class="chev"><svg width="7" height="5" viewBox="0 0 7 5"><path d="M1 1l2.5 2.5L6 1" stroke="#fff" fill="none" stroke-width="1.4"/></svg></span></div>
  <div class="faq-item" style="top:541px"><span class="q">Q:</span>I want to plant a church, what do I do?<span class="chev"><svg width="7" height="5" viewBox="0 0 7 5"><path d="M1 1l2.5 2.5L6 1" stroke="#fff" fill="none" stroke-width="1.4"/></svg></span></div>
  <div class="faq-item" style="top:609px"><span class="q">Q:</span>In what ways can I support HLS?<span class="chev"><svg width="7" height="5" viewBox="0 0 7 5"><path d="M1 1l2.5 2.5L6 1" stroke="#fff" fill="none" stroke-width="1.4"/></svg></span></div>
</section>

<footer class="site-footer">
  <h4 style="left:110px">Contact Us</h4>
  <div class="contact-line" style="top:111px"><svg width="10" height="14" viewBox="0 0 10 14"><path d="M5 14S0 7.5 0 5a5 5 0 0 1 10 0c0 2.5-5 9-5 9Z" fill="#ec6a1f"/><circle cx="5" cy="5" r="2" fill="#1d1d1d"/></svg><span>301 Lorem ipsum dolor sit amet,<br>consectetur elit,</span></div>
  <div class="contact-line" style="top:169px"><svg width="15" height="11" viewBox="0 0 15 11"><rect width="15" height="11" rx="1" fill="#ec6a1f"/><path d="M1 1l6.5 5L14 1" stroke="#1d1d1d" fill="none" stroke-width="1.4"/></svg><span>info@harborlanternseedworks.com</span></div>
  <div class="contact-line" style="top:205px"><svg width="13" height="13" viewBox="0 0 13 13"><path d="M3 0 5 4 3.5 5.5a8 8 0 0 0 4 4L9 8l4 2-1 3C5 13 0 8 0 1Z" fill="#ec6a1f"/></svg><span>(888) 888-8888</span></div>
  <div class="contact-line" style="top:240px"><svg width="14" height="13" viewBox="0 0 14 13"><rect x="0" y="3" width="14" height="10" rx="1" fill="#ec6a1f"/><rect x="3" y="0" width="8" height="5" fill="#ec6a1f"/><rect x="4" y="6" width="6" height="4" fill="#1d1d1d"/></svg><span>1 (123)&nbsp; 456 - 7890</span></div>

  <h4 style="left:461px">Links</h4>
  <span class="link" style="left:462px;top:113px">Home</span>
  <span class="link" style="left:462px;top:140px">About Us</span>
  <span class="link" style="left:462px;top:166px">Partners</span>
  <span class="link" style="left:462px;top:193px">Donate</span>
  <span class="link" style="left:551px;top:113px">Terms &amp; Condition</span>
  <span class="link" style="left:551px;top:140px">Privacy Policy</span>
  <span class="link" style="left:551px;top:166px">Support</span>
  <span class="link" style="left:551px;top:193px">Contact</span>

  <h4 style="left:728px">Subscribe for Updates</h4>
  <div class="email-field">Emaill Address</div>
  <div class="submit-btn">SUBMIT</div>
  <div class="consent"><svg width="12" height="12" viewBox="0 0 12 12"><rect x=".5" y=".5" width="11" height="11" fill="none" stroke="#fff"/><path d="M2.5 6l2.5 2.5L10 2" stroke="#fff" fill="none" stroke-width="1.6"/></svg>Yes, Please Contact me.</div>
  <span class="social" style="left:728px"></span>
  <span class="social" style="left:771px"></span>
  <span class="social" style="left:813px"></span>

  <div class="copyright">© 2021&nbsp; Harbor Lantern Seedworks&nbsp; |&nbsp; All Rights Reserved</div>
</footer>

</body>
</html>
```